Real Estate Virtual 360 Tour Web Home Page [Design Only]

see new upload mockup attached

We want new design ideas for our home page.

Link to video from web dev team of wireframe for reference: https://files.quorvantshare.net/d/7q-WpR2n8Lx4Tb6Hc0Yv9Ke3Mz5Ud/view?usp=sharing

Things desired on the home page:

Book a shoot now - Multiple markets,links to the corresponding market page for actual booking

1 Complete Package - includes Video, 3D Doviquell Tours, Exterior 360 Tours, Map, Agent Profile, Floor Plans, 2D Photos with blue sky and twilight sky guarantee

How it Works-https://clipnestra.net/582716049

Pricing-https://brisklumehomes.net/pricing/

House Search-https://brisklumehomes.net/

Footer
Updates

Target Market(s)

Real Estate Agents, Realtors, Home Buyers

Number of Pages Required

1 page

Font styles to use
Sans Serif

Colors
0555a3

Requirements
Must have
• see new upload mockup attached

Footer

```html
<!DOCTYPE html>
<html lang="en">
<head>
<meta charset="utf-8">
<title>Brisklume Homes — Real Estate Virtual 360° Tour</title>
<link rel="stylesheet" href="https://fonts.googleapis.com/css2?family=Montserrat:wght@400;500;600;700;800&display=swap">
<style>
:root{
  --navy:#1d2c74;
  --blue:#0555a3;
  --ink:#222633;
  --muted:#5d6270;
  --line:#e3e6ee;
  --soft:#eef0f5;
  --field:#f3f4f7;
  --white:#ffffff;
  --footer:#1b2a6b;
}
*{box-sizing:border-box;margin:0;padding:0}
html,body{width:1200px;height:5089px;overflow:hidden}
body{font-family:"Montserrat",sans-serif;color:var(--ink);background:var(--white);position:relative}
.abs{position:absolute}
a{color:inherit;text-decoration:none}

/* header */
.site-header{position:absolute;left:0;top:0;width:1200px;height:148px}
.brand{position:absolute;left:73px;top:28px;display:flex;align-items:center;gap:10px;font-weight:800;font-size:30px;color:var(--navy);letter-spacing:1px}
.brand .dot{width:18px;height:18px;border-radius:50%;background:var(--blue)}
.call{position:absolute;left:806px;top:24px;display:flex;gap:8px;align-items:center;color:var(--navy)}
.call small{display:block;font-size:9px;font-weight:700;color:var(--blue)}
.call b{font-size:15px}
.socials{position:absolute;left:966px;top:28px;display:flex;gap:14px}
.socials i{width:13px;height:13px;border-radius:50%;background:#8a8fa0;display:block}
.nav{position:absolute;left:432px;top:78px;display:flex;gap:27px;font-size:11.5px;font-weight:600;color:var(--navy)}
.nav .active{color:var(--blue);border-bottom:2px solid var(--blue);padding-bottom:4px}
.btn{display:inline-flex;align-items:center;gap:10px;background:var(--navy);color:var(--white);font-weight:700;font-size:13px;border-radius:6px;letter-spacing:.3px}
.nav-cta{position:absolute;left:975px;top:70px;height:32px;padding:0 14px;font-size:11px}

/* hero */
.hero-photo{position:absolute;left:0;top:148px;width:450px;height:526px;background:linear-gradient(160deg,#5b7fb5 0%,#9fb4cf 40%,#3b4b62 75%,#2d5a8a 100%)}
.hero-copy{position:absolute;left:450px;top:148px;width:750px;height:526px;background:var(--soft)}
.hero-copy h1{position:absolute;left:145px;top:136px;font-size:42px;line-height:46px;font-weight:700;color:var(--navy);letter-spacing:1px}
.hero-copy h1 span{color:var(--blue);font-weight:800}
.hero-copy p{position:absolute;left:145px;top:248px;width:450px;font-size:13.5px;line-height:18px;color:var(--muted)}
.hero-copy .btn{position:absolute;left:145px;top:350px;height:44px;padding:0 18px}
.badge{width:34px;height:24px;border-radius:12px;border:2px solid var(--white);font-size:9px;display:flex;align-items:center;justify-content:center}

/* about */
.about{position:absolute;left:0;top:674px;width:450px;height:609px}
.about h2{position:absolute;left:77px;top:108px;font-size:32px;line-height:38px;font-weight:700}
.about h2 span{color:var(--blue);display:block}
.about p{position:absolute;left:77px;width:300px;font-size:13px;line-height:19px;color:var(--muted)}
.about .btn{position:absolute;left:75px;top:458px;height:44px;padding:0 18px}
.gallery{position:absolute;left:450px;top:674px;width:750px;height:609px;display:grid;grid-template-columns:250px 250px 250px;grid-template-rows:200px 205px 204px}
.gallery div{border:1px solid var(--white)}

/* how it works */
.quote{position:absolute;left:80px;top:1360px;width:440px;text-align:center}
.quote .mark{font-size:110px;line-height:80px;font-weight:800;color:var(--navy)}
.quote p{margin-top:40px;font-size:13.5px;line-height:19px;color:var(--muted)}
.quote cite{display:block;margin-top:16px;font-style:normal;font-weight:700;font-size:14px;color:var(--blue)}
.dots{display:flex;gap:9px;align-items:center;justify-content:center}
.dots i{width:6px;height:6px;border-radius:50%;background:var(--navy)}
.dots i.on{width:16px;height:16px;background:var(--blue)}
.quote .dots{margin-top:44px}
.steps{position:absolute;left:676px;top:1360px}
.step{display:flex;align-items:center;gap:22px;height:70px;margin-bottom:10px}
.step .ico{width:64px;height:64px;border-radius:50%;border:2px solid #c9cee0;display:flex;align-items:center;justify-content:center}
.step b{font-size:14px;line-height:17px;font-weight:700;width:230px}
.vert{position:absolute;font-weight:800;font-size:32px;color:var(--navy);letter-spacing:2px;writing-mode:vertical-rl}
.vert-how{left:1086px;top:1360px}
.vert-bar{position:absolute;width:4px;background:var(--blue);border-radius:2px}

/* search */
.search-bg{position:absolute;left:0;top:1780px;width:1200px;height:454px}
.search-card{position:absolute;left:150px;top:1862px;width:898px;height:352px;background:var(--white);box-shadow:0 6px 30px rgba(30,40,80,.12)}
.search-card h2{position:absolute;left:0;width:898px;top:40px;text-align:center;font-size:28px;font-weight:700;color:var(--navy)}
.lbl{position:absolute;font-size:13px;color:var(--muted)}
.fld{position:absolute;height:38px;background:var(--field);border:1px solid var(--line);font-size:11px;color:#9a9faf;display:flex;align-items:center;justify-content:space-between;padding:0 10px}
.chk{position:absolute;display:flex;gap:8px;align-items:center;font-size:13px;color:var(--muted)}
.chk i{width:14px;height:14px;border:1px solid #c9cdd8;background:var(--white)}
.search-card .btn{position:absolute;left:382px;top:277px;width:136px;height:40px;justify-content:center;font-size:14px;border-radius:4px}

/* listings */
.listing{position:absolute;width:330px}
.listing .ph{height:188px;position:relative}
.listing .tag{position:absolute;left:0;top:10px;background:var(--navy);color:var(--white);font-size:11px;font-weight:700;padding:5px 10px}
.listing h3{margin-top:14px;font-size:14px;font-weight:700}
.listing .meta{margin-top:10px;display:flex;gap:24px;font-size:13px;color:var(--muted)}
.listing .meta span{display:flex;gap:6px;align-items:center}
.listing .meta i{width:14px;height:10px;background:var(--blue);border-radius:2px;display:block}

/* map */
.map{position:absolute;left:0;top:2896px;width:1200px;height:578px;background:linear-gradient(135deg,#e9ecef 0%,#dfe4e8 45%,#d4e4d6 70%,#e6e9ec 100%)}

/* pricing */
.vert-pricing{left:76px;top:3548px;transform:rotate(180deg)}
.tabs{position:absolute;left:256px;top:3552px;display:flex;gap:34px;font-size:13.5px;font-weight:600;color:#8d92a3}
.tabs .on{color:var(--navy)}
.arrows{position:absolute;left:1058px;top:3604px;display:flex;gap:12px}
.arrows i{width:22px;height:22px;border-radius:50%;border:1px solid var(--line);display:block}
.plan{position:absolute;top:3648px;width:299px;height:355px;background:var(--white);box-shadow:0 4px 24px rgba(30,40,80,.1)}
.plan h3{text-align:center;margin-top:30px;font-size:15px;font-weight:700;color:var(--navy)}
.plan ul{list-style:none;margin:26px 0 0 26px;font-size:13.5px;line-height:26px;color:var(--ink)}
.plan li{display:flex;gap:10px;align-items:flex-start}
.plan li svg{flex:none;margin-top:5px}
.plan .foot{position:absolute;left:0;bottom:0;width:299px;height:46px;display:flex}
.plan .price{flex:1;display:flex;align-items:center;padding-left:28px;font-size:18px;font-weight:700;color:var(--navy);border-top:1px solid var(--line)}
.plan .book{width:128px;background:var(--navy);color:var(--white);display:flex;align-items:center;justify-content:center;gap:8px;font-weight:700;font-size:14px}

/* team */
.team-title{position:absolute;left:77px;top:4240px;font-size:34px;font-weight:700;color:var(--navy)}
.team-copy{position:absolute;left:77px;width:355px;font-size:13px;line-height:19px;color:var(--muted)}
.member{position:absolute;width:196px}
.member .ph{height:194px}
.member b{display:block;margin-top:12px;font-size:13px}
.member small{display:block;font-size:12.5px;color:var(--muted)}
.member .so{display:flex;gap:12px;margin-top:8px}
.member .so i{width:10px;height:10px;border-radius:50%;background:#a5aaba;display:block}
.team-dots{position:absolute;left:780px;top:4672px}

/* footer */
.site-footer{position:absolute;left:0;top:4765px;width:1200px;height:295px;background:var(--footer);color:var(--white)}
.f-brand{position:absolute;left:92px;top:62px;display:flex;align-items:center;gap:10px;font-weight:800;font-size:30px;color:#e6e9f5;letter-spacing:1px}
.f-brand .dot{width:18px;height:18px;border-radius:50%;background:#6f7fbf}
.f-col{position:absolute;top:50px;font-size:11.5px;line-height:19px;font-weight:600}
.f-col h4{font-size:11.5px;font-weight:700;color:#aeb8e6;letter-spacing:.5px;margin-bottom:22px}
.f-col .row{display:flex;gap:8px;margin-bottom:12px}
.f-social{display:flex;gap:20px}
.f-social i{width:14px;height:14px;border-radius:50%;background:var(--white);display:block}
.copyright{position:absolute;left:0;top:5060px;width:1200px;height:29px;text-align:center;font-size:9.5px;line-height:29px;color:var(--muted);font-weight:600}
</style>
</head>
<body>

<header class="site-header">
  <div class="brand"><span class="dot"></span>BRISKLUME HOMES</div>
  <div class="call">
    <svg width="18" height="18" viewBox="0 0 24 24"><path d="M6.6 10.8a15 15 0 0 0 6.6 6.6l2.2-2.2c.3-.3.7-.4 1-.2 1.1.4 2.3.6 3.6.6.6 0 1 .4 1 1V20c0 .6-.4 1-1 1A17 17 0 0 1 3 4c0-.6.4-1 1-1h3.5c.6 0 1 .4 1 1 0 1.3.2 2.5.6 3.6.1.3 0 .7-.2 1z" fill="none" stroke="#0555a3" stroke-width="1.8"/></svg>
    <div><small>CALL US TODAY</small><b>555.014.2290</b></div>
  </div>
  <div class="socials"><i></i><i></i><i></i><i></i><i></i></div>
  <nav class="nav">
    <a class="active">HOME</a><a>ABOUT</a><a>OUR SOLUTIONS ▾</a><a>HOW IT WORKS</a><a>PRICING</a><a>CONTACT</a>
  </nav>
  <a class="btn nav-cta">BOOK A SHOOT NOW</a>
</header>

<div class="hero-photo" role="img" aria-label="Modern white house at dusk with pool"></div>
<section class="hero-copy">
  <h1>REAL ESTATE<br><span>VIRTUAL 360° TOUR</span></h1>
  <p>Lorem ipsum dolor sit amet, consectetur adipiscing elit, sed do eiusmod tempor incididunt ut labore et dolore magna aliqua. Ut enim ad minim veniam, quis nostrud exercitation ull aco laboris nisi ut aliquip ex ea commodo consequat.</p>
  <a class="btn"><span class="badge">360°</span>BOOK A SHOOT NOW</a>
</section>

<section class="about">
  <h2>About<span>Brisklume Homes</span></h2>
  <p style="top:200px">Lorem ipsum dolor sit amet, consectetur adi piscing elit, sed do eiusmod tempor incidid unt ut labore et dolore magna aliqua. Ut eni m ad minim veniam, quis nostrud exercitati on ullaco laboris nisi ut aliquip ex ea comm odo consequat.</p>
  <p style="top:338px">Duis aute irure dolor in reprehenderit in vol uptate velit esse cillum dolore eu fugiat nul la pariatur. Excepteur sint occaecat cupidat at non proident, sunt in culpa qui officia de serunt mollitanim id est laborum.</p>
  <a class="btn"><span class="badge">360°</span>BOOK A SHOOT NOW</a>
</section>
<div class="gallery">
  <div role="img" aria-label="Modern apartment balconies" style="grid-row:1/3;background:linear-gradient(180deg,#8fb2d8,#7d7466)"></div>
  <div role="img" aria-label="Aerial view of winding road through hills" style="grid-column:2/4;background:linear-gradient(135deg,#3f5a33,#7e8a62,#2f4a2c)"></div>
  <div role="img" aria-label="Suburban house lit at dusk" style="background:linear-gradient(180deg,#6d7fb6,#9a8ea8,#3d4660)"></div>
  <div role="img" aria-label="White modern house under trees" style="background:linear-gradient(180deg,#dfe6ec,#b9c1b3)"></div>
  <div role="img" aria-label="Spiral staircase building facade" style="background:linear-gradient(180deg,#b8b8b4,#6f6e6a)"></div>
  <div role="img" aria-label="Palm trees beside a beige villa" style="background:linear-gradient(180deg,#cfd9e3,#8d8f7d)"></div>
  <div role="img" aria-label="Large white house with lawn" style="background:linear-gradient(180deg,#7a8f9e,#d7d9da,#58693f)"></div>
</div>

<section aria-label="Testimonial">
  <div class="quote">
    <div class="mark">&ldquo;&rdquo;</div>
    <p>Lorem ipsum dolor sit amet, consectetur adipiscing elit, sed do eiusmod tempor incididunt ut labore et dolore magna aliqua. Ut enim ad minim veniam, quis nostrud exercitation ullamco la boris nisi ut aliquip ex ea commodo consequat. Duis aute irure dolor in reprehenderit in voluptate velit esse cillum dolore eu fugiat nulla pariatur. Excepteur sint occaecat cupidatat non proident, sunt in culpa officia deserunt mollit anim id est la borum.</p>
    <cite>- Dana Ruelle -</cite>
    <div class="dots"><i class="on"></i><i></i><i></i><i></i><i></i></div>
  </div>
</section>

<section class="steps" aria-label="How it works">
  <div class="step"><span class="ico"><svg width="26" height="32" viewBox="0 0 26 32"><rect x="3" y="2" width="20" height="28" rx="3" fill="none" stroke="#1d2c74" stroke-width="2"/><rect x="7" y="12" width="12" height="6" fill="#0555a3"/></svg></span><b>Book a shoot</b></div>
  <div class="step"><span class="ico"><svg width="32" height="28" viewBox="0 0 32 28"><rect x="2" y="4" width="28" height="22" rx="2" fill="none" stroke="#e07a2e" stroke-width="2"/><path d="M2 10h28M9 1v6M23 1v6" stroke="#e07a2e" stroke-width="2"/></svg></span><b>Schedule the Date for the shoot</b></div>
  <div class="step"><span class="ico"><svg width="34" height="24" viewBox="0 0 34 24"><ellipse cx="17" cy="12" rx="15" ry="9" fill="none" stroke="#0555a3" stroke-width="2"/><text x="17" y="16" font-size="10" font-weight="700" text-anchor="middle" fill="#0555a3" font-family="Montserrat,sans-serif">360°</text></svg></span><b>360° Shoot for your house, land or commercial</b></div>
  <div class="step"><span class="ico"><svg width="28" height="28" viewBox="0 0 28 28"><rect x="2" y="2" width="24" height="24" rx="3" fill="none" stroke="#e07a2e" stroke-width="2"/><path d="M11 8l9 6-9 6z" fill="#e07a2e"/></svg></span><b>Be happy and use the video to showcase your property</b></div>
</section>
<div class="vert vert-how">HOW IT WORKS</div>
<div class="vert-bar" style="left:1073px;top:1480px;height:160px"></div>

<div class="search-bg">
  <svg width="1200" height="454" viewBox="0 0 1200 454">
    <path d="M0 70 C300 20 500 180 800 120 S1100 40 1200 90" fill="none" stroke="#dfe2ea"/>
    <path d="M0 100 C300 40 520 210 820 150 S1100 60 1200 120" fill="none" stroke="#e6e8ee"/>
    <path d="M0 360 C300 260 600 420 900 330 S1150 300 1200 320" fill="none" stroke="#dfe2ea"/>
    <path d="M0 390 C300 290 620 450 920 360 S1150 330 1200 350" fill="none" stroke="#e6e8ee"/>
  </svg>
</div>
<section class="search-card">
  <h2>Search Houses</h2>
  <span class="lbl" style="left:38px;top:102px">Cities</span>
  <div class="fld" style="left:38px;top:128px;width:232px">Select city <span>▾</span></div>
  <span class="lbl" style="left:290px;top:102px">Price Min</span>
  <div class="fld" style="left:290px;top:128px;width:132px"></div>
  <span class="lbl" style="left:436px;top:102px">Price Max</span>
  <div class="fld" style="left:436px;top:128px;width:132px"></div>
  <span class="lbl" style="left:582px;top:102px">Min Bedrooms</span>
  <div class="fld" style="left:582px;top:128px;width:132px"></div>
  <span class="lbl" style="left:728px;top:102px">Min Bathrooms</span>
  <div class="fld" style="left:728px;top:128px;width:132px"></div>
  <span class="lbl" style="left:38px;top:180px">Property Types</span>
  <div class="fld" style="left:38px;top:206px;width:232px">For rent and for sale <span>▾</span></div>
  <span class="chk" style="left:290px;top:217px"><i></i>Garage</span>
  <span class="chk" style="left:386px;top:217px"><i></i>Basement</span>
  <span class="lbl" style="left:496px;top:180px">Show Houses Within</span>
  <div class="fld" style="left:496px;top:206px;width:102px">20 <span>▾</span></div>
  <div class="fld" style="left:610px;top:206px;width:102px">mi <span>▾</span></div>
  <span class="lbl" style="left:728px;top:180px">of Location Name</span>
  <div class="fld" style="left:728px;top:206px;width:132px"></div>
  <span class="lbl" style="left:734px;top:255px;font-size:12px">⌖ Use My Location</span>
  <a class="btn">SEARCH</a>
</section>

<section aria-label="Listings">
  <article class="listing" style="left:75px;top:2293px"><div class="ph" role="img" aria-label="Two-storey house with garage" style="background:linear-gradient(180deg,#a9bed1,#7f8079,#5e6b4a)"><span class="tag">FOR SALE</span></div><h3>412 Birchwood Dr Fort Collins, CO 80525</h3><div class="meta"><span><i></i>Beds: 3</span><span><i></i>Baths: 3</span><span><i></i>2355 ft²</span></div></article>
  <article class="listing" style="left:435px;top:2293px"><div class="ph" role="img" aria-label="Mountain home in snow" style="background:linear-gradient(180deg,#6a8fc0,#b58a55,#e9eef3)"><span class="tag">FOR SALE</span></div><h3>9340 Hollow Pine Rd Conifer, CO 80433</h3><div class="meta"><span><i></i>Beds: 2</span><span><i></i>Baths: 2</span><span><i></i>1573 ft²</span></div></article>
  <article class="listing" style="left:795px;top:2293px"><div class="ph" role="img" aria-label="Stone house with triple garage" style="background:linear-gradient(180deg,#8ea9c6,#7a7468,#c9cdd1)"><span class="tag">FOR SALE</span></div><h3>7715 Quarry Hill Dr Evergreen, CO 80439</h3><div class="meta"><span><i></i>Beds: 4</span><span><i></i>Baths: 5</span><span><i></i>3929 ft²</span></div></article>
  <article class="listing" style="left:75px;top:2578px"><div class="ph" role="img" aria-label="Aerial view of house among trees" style="background:linear-gradient(180deg,#6b7a52,#9a8a76,#5d6d45)"><span class="tag">FOR SALE</span></div><h3>8824 W 41st Ave Wheat Ridge, CO 80033</h3><div class="meta"><span><i></i>Beds: 3</span><span><i></i>Baths: 2</span><span><i></i>2355 ft²</span></div></article>
  <article class="listing" style="left:435px;top:2578px"><div class="ph" role="img" aria-label="Single-storey home with driveway" style="background:linear-gradient(180deg,#8fb0d6,#c6b8a4,#9a958d)"><span class="tag">FOR SALE</span></div><h3>1508 8th St UNIT B Greeley, CO 80631</h3><div class="meta"><span><i></i>Beds: 3</span><span><i></i>Baths: 2</span><span><i></i>1573 ft²</span></div></article>
  <article class="listing" style="left:795px;top:2578px"><div class="ph" role="img" aria-label="Farmhouse with wide lawn" style="background:linear-gradient(180deg,#7ea3d0,#d9dcdd,#6f8b4a)"><span class="tag">FOR SALE</span></div><h3>3126 Cobble Ln Johnstown, CO 80534</h3><div class="meta"><span><i></i>Beds: 3</span><span><i></i>Baths: 3</span><span><i></i>3929 ft²</span></div></article>
</section>

<div class="map" role="img" aria-label="Street map of the area showing listing locations"></div>

<div class="vert vert-pricing">OUR PRICING</div>
<div class="vert-bar" style="left:118px;top:3550px;height:150px"></div>
<nav class="tabs"><span class="on">▸ Brisklume Tour Shot</span><span>Land Package</span><span>Commercial Properties (10,000 sq ft)</span><span>Big Box Commercial</span></nav>
<div class="arrows"><i></i><i></i></div>

<section aria-label="Pricing plans">
  <article class="plan" style="left:166px">
    <h3>1100 Total Sq Ft or Less</h3>
    <ul>
      <li><svg width="14" height="14"><circle cx="7" cy="7" r="6" fill="none" stroke="#222633"/><path d="M5 4l3 3-3 3" fill="none" stroke="#222633"/></svg>Video</li>
      <li><svg width="14" height="14"><circle cx="7" cy="7" r="6" fill="none" stroke="#222633"/><path d="M5 4l3 3-3 3" fill="none" stroke="#222633"/></svg>3D Doviquell Tours</li>
      <li><svg width="14" height="14"><circle cx="7" cy="7" r="6" fill="none" stroke="#222633"/><path d="M5 4l3 3-3 3" fill="none" stroke="#222633"/></svg>Exterior 360 Tours</li>
      <li><svg width="14" height="14"><circle cx="7" cy="7" r="6" fill="none" stroke="#222633"/><path d="M5 4l3 3-3 3" fill="none" stroke="#222633"/></svg>Map</li>
      <li><svg width="14" height="14"><circle cx="7" cy="7" r="6" fill="none" stroke="#222633"/><path d="M5 4l3 3-3 3" fill="none" stroke="#222633"/></svg>Agent Profile</li>
      <li><svg width="14" height="14"><circle cx="7" cy="7" r="6" fill="none" stroke="#222633"/><path d="M5 4l3 3-3 3" fill="none" stroke="#222633"/></svg>Floor Plans</li>
      <li><svg width="14" height="14"><circle cx="7" cy="7" r="6" fill="none" stroke="#222633"/><path d="M5 4l3 3-3 3" fill="none" stroke="#222633"/></svg>2D Photos with blue sky and<br>twilight sky guarantee</li>
    </ul>
    <div class="foot"><span class="price">USD 249.00</span><a class="book">→ BOOK</a></div>
  </article>
  <article class="plan" style="left:496px">
    <h3>1101-2700 Total Sq Ft</h3>
    <ul>
      <li><svg width="14" height="14"><circle cx="7" cy="7" r="6" fill="none" stroke="#222633"/><path d="M5 4l3 3-3 3" fill="none" stroke="#222633"/></svg>Video</li>
      <li><svg width="14" height="14"><circle cx="7" cy="7" r="6" fill="none" stroke="#222633"/><path d="M5 4l3 3-3 3" fill="none" stroke="#222633"/></svg>3D Doviquell Tours</li>
      <li><svg width="14" height="14"><circle cx="7" cy="7" r="6" fill="none" stroke="#222633"/><path d="M5 4l3 3-3 3" fill="none" stroke="#222633"/></svg>Exterior 360 Tours</li>
      <li><svg width="14" height="14"><circle cx="7" cy="7" r="6" fill="none" stroke="#222633"/><path d="M5 4l3 3-3 3" fill="none" stroke="#222633"/></svg>Map</li>
      <li><svg width="14" height="14"><circle cx="7" cy="7" r="6" fill="none" stroke="#222633"/><path d="M5 4l3 3-3 3" fill="none" stroke="#222633"/></svg>Agent Profile</li>
      <li><svg width="14" height="14"><circle cx="7" cy="7" r="6" fill="none" stroke="#222633"/><path d="M5 4l3 3-3 3" fill="none" stroke="#222633"/></svg>Floor Plans</li>
      <li><svg width="14" height="14"><circle cx="7" cy="7" r="6" fill="none" stroke="#222633"/><path d="M5 4l3 3-3 3" fill="none" stroke="#222633"/></svg>2D Photos with blue sky and<br>twilight sky guarantee</li>
    </ul>
    <div class="foot"><span class="price">USD 299.00</span><a class="book">→ BOOK</a></div>
  </article>
  <article class="plan" style="left:826px">
    <h3>2700-4200 Total Sq Ft</h3>
    <ul>
      <li><svg width="14" height="14"><circle cx="7" cy="7" r="6" fill="none" stroke="#222633"/><path d="M5 4l3 3-3 3" fill="none" stroke="#222633"/></svg>Video</li>
      <li><svg width="14" height="14"><circle cx="7" cy="7" r="6" fill="none" stroke="#222633"/><path d="M5 4l3 3-3 3" fill="none" stroke="#222633"/></svg>3D Doviquell Tours</li>
      <li><svg width="14" height="14"><circle cx="7" cy="7" r="6" fill="none" stroke="#222633"/><path d="M5 4l3 3-3 3" fill="none" stroke="#222633"/></svg>Exterior 360 Tours</li>
      <li><svg width="14" height="14"><circle cx="7" cy="7" r="6" fill="none" stroke="#222633"/><path d="M5 4l3 3-3 3" fill="none" stroke="#222633"/></svg>Map</li>
      <li><svg width="14" height="14"><circle cx="7" cy="7" r="6" fill="none" stroke="#222633"/><path d="M5 4l3 3-3 3" fill="none" stroke="#222633"/></svg>Agent Profile</li>
      <li><svg width="14" height="14"><circle cx="7" cy="7" r="6" fill="none" stroke="#222633"/><path d="M5 4l3 3-3 3" fill="none" stroke="#222633"/></svg>Floor Plans</li>
      <li><svg width="14" height="14"><circle cx="7" cy="7" r="6" fill="none" stroke="#222633"/><path d="M5 4l3 3-3 3" fill="none" stroke="#222633"/></svg>2D Photos with blue sky and<br>twilight sky guarantee</li>
    </ul>
    <div class="foot"><span class="price">USD 399.00</span><a class="book">→ BOOK</a></div>
  </article>
</section>

<section aria-label="Our team">
  <h2 class="team-title">Our Team</h2>
  <p class="team-copy" style="top:4306px">Lorem ipsum dolor sit amet, consectetur adipiscing elit, sed do eiusmod tempor incididunt ut labore et dolore magna aliqua. Ut enim ad minim veniam, qu is nostrud exercitation ullaco laboris nisi ut aliquip ex ea commodo consequat.</p>
  <p class="team-copy" style="top:4412px">Duis aute irure dolor in reprehenderit in voluptate velit esse cillum dolore eu fugiat nulla pariatur. Ex cepteur sint occaecat cupidatat non proident.</p>
  <div class="member" style="left:518px;top:4079px"><div class="ph" role="img" aria-label="Portrait of team member" style="background:linear-gradient(180deg,#e7e9ec,#9aa4b3)"></div><b>Owen Calder</b><small>CEO</small><div class="so"><i></i><i></i><i></i><i></i></div></div>
  <div class="member" style="left:727px;top:4079px"><div class="ph" role="img" aria-label="Portrait of team member" style="background:linear-gradient(180deg,#c9b79d,#4b5266)"></div><b>Tobin Hale</b><small>COO</small><div class="so"><i></i><i></i><i></i><i></i></div></div>
  <div class="member" style="left:937px;top:4079px"><div class="ph" role="img" aria-label="Portrait of team member" style="background:linear-gradient(180deg,#a25d44,#2f3240)"></div><b>Felix Marsh</b><small>CFO</small><div class="so"><i></i><i></i><i></i><i></i></div></div>
  <div class="member" style="left:518px;top:4371px"><div class="ph" role="img" aria-label="Portrait of team member" style="background:linear-gradient(180deg,#c8cdd4,#2f4a8a)"></div><b>Reid Ashby</b><small>Associate</small><div class="so"><i></i><i></i><i></i><i></i></div></div>
  <div class="member" style="left:727px;top:4371px"><div class="ph" role="img" aria-label="Portrait of team member" style="background:linear-gradient(180deg,#b7b99a,#6f6a5c)"></div><b>Nora Vance</b><small>Associate</small><div class="so"><i></i><i></i><i></i><i></i></div></div>
  <div class="member" style="left:937px;top:4371px"><div class="ph" role="img" aria-label="Portrait of team member" style="background:linear-gradient(180deg,#e4e2de,#8a6f5c)"></div><b>Lena Sorrel</b><small>Associate</small><div class="so"><i></i><i></i><i></i><i></i></div></div>
  <div class="dots team-dots"><i class="on"></i><i></i><i></i><i></i><i></i></div>
</section>

<footer class="site-footer">
  <div class="f-brand"><span class="dot"></span>BRISKLUME HOMES</div>
  <div class="f-col" style="left:352px"><h4>NAVIGATION</h4>Home<br>About<br>Our Solutions<br>How It Works<br>Pricing<br>Contact</div>
  <div class="f-col" style="left:515px"><h4>OUR SOLUTIONS</h4>Houses<br>Land<br>Commercial</div>
  <div class="f-col" style="left:693px"><h4>CONTACT</h4>
    <div class="row"><span>⌖</span><span>Brisklume Homes<br>118 Marlow Ave<br>Fort Collins, CO 80524</span></div>
    <div class="row"><span>✆</span><span>555-018-4471</span></div>
    <div class="row"><span>✉</span><span>hello@brisklumehomes.net</span></div>
  </div>
  <div class="f-col" style="left:938px"><h4>FOLLOW US</h4><div class="f-social"><i></i><i></i><i></i><i></i><i></i></div></div>
</footer>
<div class="copyright">COPYRIGHT © 2020 BRISKLUME HOMES. ALL RIGHTS RESERVED.</div>

</body>
</html>
```